Website Design for Professional Services Company

• Create a new website design that is easy to maintain inside of WordPress with a main page design, a design for generic content pages, and a design for customer case studies. Our current design relies on a number of plugins to function, and we would like to get away from that as much as possible. Our current design also requires a fair amount of coding that we would like to get away from. The more we can use native WordPress the better. We are not opposed to a small subset of plugins that are widely used and readily updated. Our current website can be found at https://brindlecrestconsulting.com/. Our fonts (for use in graphics, we don’t want custom fonts on the website itself to make sure it always displays correctly) and colors are as follows:
o Brindlecrest Blue:
 #1b75bc
o Brindlecrest Grey:
 #6d6f71
o Main Font:
 Telegrafico
o Accent Font:
 Nexa Light

```html
<!DOCTYPE html>
<html lang="en">
<head>
<meta charset="utf-8">
<title>Brindlecrest Consulting</title>
<link href="https://fonts.googleapis.com/css2?family=Lexend+Giga:wght@500&family=Nunito+Sans:wght@400;600;700&display=swap" rel="stylesheet">
<style>
:root{
  --blue:#1b75bc;
  --grey:#6d6f71;
  --dark:#5d5f61;
  --ink:#1f1f1f;
  --text:#6a6a6a;
  --light:#f1f1f1;
  --white:#ffffff;
}
*{box-sizing:border-box;margin:0;padding:0}
html,body{width:1200px;height:3205px;overflow:hidden;background:var(--white)}
body{font-family:"Nunito Sans",sans-serif;color:var(--ink)}
.page{position:relative;width:1200px;height:3205px;overflow:hidden}
.abs{position:absolute}
.heading{font-family:"Lexend Giga",sans-serif;font-weight:500;letter-spacing:3px;text-transform:uppercase}
.btn{position:absolute;background:var(--blue);color:var(--white);font-weight:600;display:flex;align-items:center;justify-content:center}

/* top bar + nav */
.topbar{position:absolute;left:0;top:0;width:1200px;height:27px;background:var(--grey);color:#fff;font-size:13px}
.topbar span{position:absolute;top:5px}
.dot{display:inline-block;width:9px;height:9px;border-radius:50%;background:#fff;margin-left:7px;vertical-align:middle}
.notch{position:absolute;left:488px;top:0;width:224px;height:27px;background:#fff;clip-path:polygon(0 0,100% 0,92% 100%,8% 100%)}
.nav{position:absolute;left:0;top:27px;width:1200px;height:63px;background:#fff;border-bottom:1px solid #e4e4e4;font-size:15px;font-weight:600}
.nav a{position:absolute;top:0;height:63px;display:flex;align-items:center;justify-content:center;color:var(--ink);text-decoration:none}
.nav .sep{position:absolute;top:0;width:1px;height:63px;background:#e4e4e4}
.brand{position:absolute;left:530px;top:22px;width:140px;text-align:center;color:var(--blue);font-weight:700;font-size:17px;letter-spacing:1px}
.brand small{display:block;font-size:8px;letter-spacing:2px;font-weight:600}

/* hero */
.hero-photo{position:absolute;left:0;top:90px;width:1200px;height:582px;
  background:linear-gradient(180deg,#eef0f2 0%,#d9dde1 45%,#8c8f93 100%);
  clip-path:polygon(0 0,100% 0,100% 86%,600px 100%,0 86%)}
.hero-title{position:absolute;top:140px;width:1200px;text-align:center;font-size:36px}
.hero-sub{position:absolute;top:200px;width:1200px;text-align:center;font-size:16px;font-weight:600}

/* sections */
.sec-title{position:absolute;width:1200px;text-align:center;font-size:29px}
.sec-sub{position:absolute;width:1200px;text-align:center;font-size:16px;color:#444}

.card{position:absolute;background:#fff;box-shadow:0 2px 10px rgba(0,0,0,.12);text-align:center}
.card .img{position:absolute;left:4px;top:4px;right:4px}
.card h3{position:absolute;left:0;right:0;font-size:16.5px;font-weight:700}
.card p{position:absolute;left:20px;right:20px;font-size:12.5px;line-height:23px;color:var(--text)}
.card .more{position:absolute;left:0;right:0;font-size:14px;color:var(--blue);font-weight:600}
.card.active{background:var(--blue);color:#fff}
.card.active p,.card.active .more{color:#fff}
.icon-badge{position:absolute;width:62px;height:62px;border-radius:50%;background:var(--blue);border:3px solid #fff;display:flex;align-items:center;justify-content:center}
.arrow-btn{position:absolute;width:38px;height:38px;border-radius:50%;background:#fff;box-shadow:0 1px 6px rgba(0,0,0,.2);display:flex;align-items:center;justify-content:center}

.about{position:absolute;left:0;top:1348px;width:1200px;height:455px;
  background:linear-gradient(90deg,#1b75bc 0%,#2a7fc0 40%,#6f98b9 60%,#b9c7d2 100%)}
.about p{position:absolute;left:144px;width:430px;color:#fff;font-size:13.5px;line-height:25.5px}

.post{position:absolute;background:#fff;box-shadow:0 2px 10px rgba(0,0,0,.1);text-align:center}
.post .img{position:absolute;left:0;top:0;width:100%;height:209px}
.post .date{position:absolute;top:193px;left:50%;transform:translateX(-50%);background:var(--blue);color:#fff;font-size:13px;font-weight:600;padding:6px 16px;white-space:nowrap}
.post .meta{position:absolute;top:245px;left:0;right:0;font-size:11.5px;color:var(--text)}
.post h4{position:absolute;top:273px;left:0;right:0;font-size:15px;font-weight:600}
.post p{position:absolute;top:302px;left:18px;right:18px;font-size:12.5px;line-height:23px;color:var(--text)}
.post .more{position:absolute;top:361px;left:0;right:0;font-size:14px;color:var(--blue);font-weight:600}

.newsletter{position:absolute;left:0;top:2460px;width:1200px;height:420px;background:var(--light)}
.footer-field{position:absolute;left:144px;width:252px;height:41px;background:#fff;font-size:11px;color:#555;padding:14px 17px}
.footer-h{position:absolute;color:#fff;font-size:21px;font-weight:700}
.detail{position:absolute;left:548px;color:#fff}
.detail b{display:block;font-size:14px;font-weight:600}
.detail span{display:block;font-size:11px;line-height:22px}
.ring{position:absolute;left:497px;width:38px;height:38px;border-radius:50%;border:2px solid #fff;display:flex;align-items:center;justify-content:center}
.rule{position:absolute;left:497px;width:260px;border-top:1px dashed rgba(255,255,255,.4)}
</style>
</head>
<body>
<div class="page">

  <!-- top bar -->
  <div class="topbar">
    <span style="left:143px">Follow Us:<i class="dot"></i><i class="dot"></i></span>
    <span style="left:296px">&#9742; (555) 010-4821</span>
    <span style="left:755px">&#9993; info@brindlecrestconsulting.com</span>
    <span style="left:992px;text-decoration:underline">Search</span>
  </div>
  <div class="notch"></div>

  <nav class="nav">
    <a style="left:140px;width:70px;color:var(--blue)">HOME</a>
    <div class="sep" style="left:209px"></div>
    <a style="left:210px;width:134px">ABOUT US</a>
    <div class="sep" style="left:344px"></div>
    <a style="left:345px;width:128px">SERVICES</a>
    <a style="left:712px;width:72px">BLOG</a>
    <div class="sep" style="left:800px"></div>
    <a style="left:801px;width:122px">CONTACT</a>
    <a style="left:925px;width:131px;background:var(--blue);color:#fff">GET IN TOUCH</a>
  </nav>
  <div class="brand">BRINDLECREST<small>CONSULTING</small></div>

  <!-- hero -->
  <div class="hero-photo" role="img" aria-label="Four business colleagues smiling and talking around a meeting table"></div>
  <svg class="abs" style="left:0;top:580px" width="1200" height="100" viewBox="0 0 1200 100">
    <path d="M145 15 L600 72 L1055 15 L1055 12 L600 60 L145 12 Z" fill="var(--blue)"/>
    <path d="M145 15 Q400 40 600 92 Q800 40 1055 15 L600 72 Z" fill="var(--blue)"/>
  </svg>
  <h1 class="hero-title heading">Brindlecrest Consulting</h1>
  <div class="hero-sub">Innovative EPM Solutions for Finance and Beyond</div>
  <div class="btn" style="left:519px;top:240px;width:161px;height:45px;font-size:16px">Discover More &nbsp;&rsaquo;</div>

  <!-- services -->
  <h2 class="sec-title heading" style="top:734px">Our Services</h2>
  <div class="sec-sub" style="top:790px">Brindlecrest Consulting offers services across the entire stack of on-premises and cloud products from Meridian.</div>

  <div class="arrow-btn" style="left:71px;top:1016px"><svg width="12" height="12" viewBox="0 0 12 12"><path d="M8 1 L3 6 L8 11" stroke="#222" stroke-width="2" fill="none"/></svg></div>
  <div class="arrow-btn" style="left:1091px;top:1016px"><svg width="12" height="12" viewBox="0 0 12 12"><path d="M4 1 L9 6 L4 11" stroke="#222" stroke-width="2" fill="none"/></svg></div>

  <div class="card" style="left:145px;top:853px;width:289px;height:366px">
    <div class="img" role="img" aria-label="Team reviewing budgets at a laptop in an office" style="height:210px;background:linear-gradient(160deg,#dfe3e7,#8e959c)"></div>
    <div class="icon-badge" style="left:113px;top:157px"><svg width="28" height="28" viewBox="0 0 28 28" fill="none" stroke="#fff" stroke-width="2"><circle cx="16" cy="10" r="6"/><path d="M3 20 L9 20 L15 23 L25 17"/></svg></div>
    <h3 style="top:238px">Budgeting and Forecasting</h3>
    <p style="top:264px">Brindlecrest specializes in both cloud and on-premise EPM solutions provided</p>
    <div class="more" style="top:326px">Learn More &nbsp;&rsaquo;</div>
  </div>

  <div class="card active" style="left:456px;top:878px;width:290px;height:366px">
    <div class="img" role="img" aria-label="Colleagues discussing work on a tablet in a bright office" style="height:210px;background:linear-gradient(160deg,#e3e6ea,#9aa0a6)"></div>
    <div class="icon-badge" style="left:114px;top:157px;background:#6d6f71"><svg width="30" height="30" viewBox="0 0 30 30" fill="none" stroke="#fff" stroke-width="2"><circle cx="15" cy="6" r="3"/><path d="M15 9 V15 M6 15 H24 M6 15 V19 M15 15 V19 M24 15 V19"/><circle cx="6" cy="22" r="3"/><circle cx="15" cy="22" r="3"/><circle cx="24" cy="22" r="3"/></svg></div>
    <h3 style="top:237px">Close and Consolidation</h3>
    <p style="top:263px">Brindlecrest specializes in both cloud and on-premise EPM solutions provided</p>
    <div class="more" style="top:324px;text-decoration:underline">Learn More &nbsp;&rsaquo;</div>
  </div>

  <div class="card" style="left:768px;top:853px;width:288px;height:366px">
    <div class="img" role="img" aria-label="Business people reviewing reports on a tablet" style="height:210px;background:linear-gradient(160deg,#e2e4e7,#7f878f)"></div>
    <div class="icon-badge" style="left:113px;top:157px"><svg width="28" height="28" viewBox="0 0 28 28" fill="none" stroke="#fff" stroke-width="2"><circle cx="13" cy="13" r="9"/><path d="M9 17 V12 M13 17 V9 M17 17 V13 M20 20 L26 26"/></svg></div>
    <h3 style="top:238px">Reporting and Analysis</h3>
    <p style="top:264px">Traditionally, Helios Planning and the Meridian EPM stack were products</p>
    <div class="more" style="top:326px">Learn More &nbsp;&rsaquo;</div>
  </div>

  <!-- about -->
  <div class="about">
    <div class="abs" role="img" aria-label="Two professionals in conversation at a desk" style="left:560px;top:0;width:640px;height:455px;background:linear-gradient(90deg,rgba(27,117,188,0),rgba(120,140,160,.5))"></div>
    <h2 class="heading abs" style="left:144px;top:76px;color:#fff;font-size:29px">About Us</h2>
    <p style="top:125px">Lorem ipsum dolor sit amet, consectetur adipiscing elit, sed do eiusmod tempor incididunt ut labore et dolore magna aliqua. Ut enim ad minim veniam, quis nostrud exercitation ullamco laboris nisi ut aliquip ex ea commodo consequat.</p>
    <p style="top:239px">Sed ut perspiciatis unde omnis iste natus error sit voluptatem accusantium doloremque laudantium, totam rem aperiam, eaque ipsa quae ab illo inventore veritatis quasi</p>
    <div class="btn" style="left:145px;top:337px;width:135px;height:39px;background:#fff;color:var(--blue);font-size:15px">Learn More &nbsp;&rsaquo;</div>
  </div>

  <!-- blog -->
  <h2 class="sec-title heading" style="top:1888px">Recent Blog Posts</h2>

  <div class="post" style="left:144px;top:1961px;width:293px;height:395px">
    <div class="img" role="img" aria-label="Hands holding a newspaper beside a cup of tea" style="background:linear-gradient(160deg,#a9adb1,#5e6266)"></div>
    <div class="date">&#9638; October 6, 2022</div>
    <div class="meta">&#9679; Dana Whitfield &nbsp;|&nbsp; &#9670; Meridian Cloud EPM</div>
    <h4>Meridian Cloud EPM Updates</h4>
    <p>Welcome back to the Brindlecrest Consulting monthly(ish) Meridian Cloud EPM</p>
    <div class="more">Read More &nbsp;&rsaquo;</div>
  </div>

  <div class="post" style="left:454px;top:1961px;width:292px;height:395px;box-shadow:0 3px 14px rgba(0,0,0,.2)">
    <div class="img" role="img" aria-label="Conference event banner over a resort at dusk" style="background:linear-gradient(180deg,#2f5d9a,#4e8a6a)"></div>
    <div class="date">&#9638; March 8, 2022</div>
    <div class="meta">&#9679; Owen Castell &nbsp;|&nbsp; &#9670; EPMUG</div>
    <h4>Speaking at Summit22!</h4>
    <p>I'm extremely honored and excited to shared that I will be presenting at</p>
    <div class="more" style="text-decoration:underline">Read More &nbsp;&rsaquo;</div>
  </div>

  <div class="post" style="left:762px;top:1961px;width:294px;height:395px">
    <div class="img" role="img" aria-label="Chalkboard with a maze and a hand drawing a way out" style="background:linear-gradient(160deg,#6b6e71,#3d4043)"></div>
    <div class="date">&#9638; November 10, 2021</div>
    <div class="meta">&#9679; Reid Lomax &nbsp;|&nbsp; &#9670; Workarounds</div>
    <h4>Management Reporting Quirk</h4>
    <p>The new built-in Management Reporting module is amazing. It is fast, intuitive,</p>
    <div class="more">Read More &nbsp;&rsaquo;</div>
  </div>

  <svg class="abs" style="left:574px;top:2388px" width="52" height="10">
    <circle cx="6" cy="5" r="3.5" fill="#ccc"/><circle cx="19" cy="5" r="3.5" fill="var(--blue)"/><circle cx="32" cy="5" r="3.5" fill="#ccc"/><circle cx="45" cy="5" r="3.5" fill="#ccc"/>
  </svg>

  <!-- newsletter -->
  <div class="newsletter"></div>
  <div class="abs" style="top:2514px;width:1200px;text-align:center;color:var(--blue);font-size:14px;font-style:italic">Ready To Take Action?</div>
  <h2 class="sec-title heading" style="top:2550px">Newsletter Signup</h2>
  <div class="sec-sub" style="top:2603px;font-size:17.5px">Subscribe to our newsletter to see the latest content we have to offer</div>
  <div class="abs" style="left:336px;top:2652px;width:524px;height:44px;background:#fff;border:1px solid #ddd;font-size:11px;color:#666;padding:15px 20px">Enter Your Email Address</div>
  <div class="btn" style="left:699px;top:2652px;width:161px;height:44px;font-size:16px">Submit Now &nbsp;&rsaquo;</div>

  <!-- footer -->
  <svg class="abs" style="left:0;top:2755px" width="1200" height="450" viewBox="0 0 1200 450">
    <path d="M0 120 L600 40 L1200 120 L1200 450 L0 450 Z" fill="var(--grey)"/>
    <path d="M150 88 Q420 40 600 6 Q780 40 1050 88 L600 34 Z" fill="var(--blue)"/>
  </svg>

  <div class="footer-h" style="left:143px;top:2885px">Contact</div>
  <div class="footer-field" style="top:2933px">Name</div>
  <div class="footer-field" style="top:2983px">Email</div>
  <div class="footer-field" style="top:3033px">Phone</div>
  <div class="footer-field" style="top:3083px">Message</div>
  <div class="btn" style="left:144px;top:3132px;width:252px;height:41px;font-size:14px">Submit Now</div>

  <div class="abs" style="left:451px;top:2935px;height:240px;border-left:1px dashed rgba(255,255,255,.35)"></div>
  <div class="abs" style="left:795px;top:2935px;height:240px;border-left:1px dashed rgba(255,255,255,.35)"></div>

  <div class="footer-h" style="left:497px;top:2885px">Contact Details</div>
  <div class="ring" style="top:2958px"><svg width="14" height="18" viewBox="0 0 14 18"><path d="M7 1 C3 1 1 4 1 7 C1 11 7 17 7 17 C7 17 13 11 13 7 C13 4 11 1 7 1 Z" fill="none" stroke="#fff" stroke-width="1.8"/><circle cx="7" cy="7" r="2" fill="#fff"/></svg></div>
  <div class="detail" style="top:2928px"><b>Address</b><span>2480 Harlow Avenue, Suite 100,<br>Fairview, Texas 75000</span></div>
  <div class="rule" style="top:3013px"></div>
  <div class="ring" style="top:3041px"><svg width="16" height="16" viewBox="0 0 16 16"><path d="M3 1 L6 1 L7 5 L5 6 C6 8 8 10 10 11 L11 9 L15 10 L15 13 C15 14 14 15 13 15 C6 15 1 10 1 3 C1 2 2 1 3 1 Z" fill="#fff"/></svg></div>
  <div class="detail" style="top:3033px"><b>Phone</b><span>(555) 010-4821</span></div>
  <div class="rule" style="top:3097px"></div>
  <div class="ring" style="top:3121px"><svg width="16" height="12" viewBox="0 0 16 12"><rect x="1" y="1" width="14" height="10" fill="none" stroke="#fff" stroke-width="1.6"/><path d="M1 1 L8 7 L15 1" fill="none" stroke="#fff" stroke-width="1.6"/></svg></div>
  <div class="detail" style="top:3114px"><b>Email Address</b><span>info@brindlecrestconsulting.com</span></div>

  <div class="abs" style="left:820px;top:3040px;width:226px;text-align:center;color:#fff;font-size:21px;font-weight:700;letter-spacing:1px">BRINDLECREST</div>
  <div class="abs" style="left:820px;top:3096px;width:226px;text-align:center;color:#fff;font-size:16px">Follow Us: <i class="dot"></i><i class="dot"></i></div>
  <div class="abs" style="left:820px;top:3137px;width:226px;text-align:center;color:#fff;font-size:14px">&copy; 2024 Brindlecrest Consulting.</div>

</div>
</body>
</html>
```